New Business Card Design Project

New business card design required for an electrical business in Australia. Offering quality electrical services including design and installation. Electrical services offered are domestic, commercial and industrial. Also meets all the air conditioning installation and maintenance needs.

Target Market(s)

The business is sleek, professional and caters primarily to wealthy clients and government contracts looking for exceptional, tailored service.

Industry/Entity Type

Electrical

Contact Information for Business Card

Gareth Pollwick (Director)
0438 692 174
admin@rvoelectrical.com.au
www.rvoelectrical.com.au

Font styles to use
Sans Serif

Requirements
Must have
• The business card must show the license number - 64139 to comply with legislation.
Nice to have
• The logo colours and fonts could be incorporated into the design if the designer sees fit. We are open to new ideas and welcome creativity. The logo style guide is attached for reference if required.

```html
<!DOCTYPE html>
<html lang="en">
<head>
<meta charset="utf-8">
<title>RVO Electrical – Business Card</title>
<link rel="stylesheet" href="https://fonts.googleapis.com/css2?family=Montserrat:wght@400;500;700&display=swap">
<style>
  :root {
    --backdrop: #92959a;
    --card: #e3e3e3;
    --navy: #132a55;
    --ink: #3d3f44;
    --divider: #132a55;
  }
  html, body {
    margin: 0;
    padding: 0;
    width: 1200px;
    height: 900px;
    overflow: hidden;
    background: var(--backdrop);
    font-family: "Montserrat", Arial, sans-serif;
  }
  .canvas {
    position: relative;
    width: 1200px;
    height: 900px;
  }
  .card {
    position: absolute;
    left: 379px;
    width: 443px;
    height: 271px;
    border-radius: 24px;
    background: var(--card);
  }
  .card--front { top: 145px; }
  .card--back { top: 484px; }

  .brand {
    position: absolute;
    left: 116px;
    top: 88px;
    width: 212px;
    color: var(--navy);
    font-weight: 700;
    text-align: right;
  }
  .brand__name {
    display: block;
    font-size: 72px;
    line-height: 72px;
    letter-spacing: 1px;
    text-align: left;
  }
  .brand__sub {
    display: block;
    margin-top: 2px;
    font-size: 17px;
    line-height: 17px;
    letter-spacing: 3px;
    margin-right: -3px;
  }

  .contact-block {
    position: absolute;
    top: 117px;
    left: 0;
    right: 0;
    height: 36px;
  }
  .person {
    position: absolute;
    right: 236px;
    top: 4px;
    text-align: right;
  }
  .person__name {
    color: var(--navy);
    font-weight: 700;
    font-size: 12px;
    letter-spacing: 0.6px;
    line-height: 1;
  }
  .person__role {
    margin-top: 6px;
    color: var(--ink);
    font-size: 10px;
    line-height: 1;
  }
  .divider {
    position: absolute;
    left: 221px;
    top: 0;
    width: 1.5px;
    height: 36px;
    background: var(--divider);
  }
  .details {
    position: absolute;
    left: 233px;
    top: -2px;
    margin: 0;
    padding: 0;
    list-style: none;
  }
  .details li {
    display: flex;
    align-items: center;
    height: 14px;
    color: var(--ink);
    font-size: 10px;
    letter-spacing: 0.2px;
  }
  .details svg {
    width: 8px;
    height: 8px;
    margin-right: 7px;
    fill: var(--navy);
    flex: none;
  }
  .licence {
    position: absolute;
    left: 0;
    right: 0;
    bottom: 26px;
    text-align: center;
    color: var(--ink);
    font-size: 9px;
    letter-spacing: 0.8px;
  }
</style>
</head>
<body>
<main class="canvas">
  <section class="card card--front">
    <div class="brand">
      <span class="brand__name">RVO</span>
      <span class="brand__sub">ELECTRICAL</span>
    </div>
  </section>

  <section class="card card--back">
    <div class="contact-block">
      <div class="person">
        <div class="person__name">GARETH POLLWICK</div>
        <div class="person__role">Director</div>
      </div>
      <div class="divider"></div>
      <ul class="details">
        <li>
          <svg viewBox="0 0 10 10" aria-hidden="true"><path d="M2 0.5l2 2-1 1.3c.6 1.3 1.6 2.3 2.9 2.9l1.3-1 2 2-1.2 1.6C4.5 9 1 5.5.4 1.7z"/></svg>
          0438 692 174
        </li>
        <li>
          <svg viewBox="0 0 10 10" aria-hidden="true"><path d="M0 2h10v6H0z M0.5 2.3L5 5.6 9.5 2.3" stroke="#e3e3e3" stroke-width="0.8"/></svg>
          admin@rvoelectrical.com.au
        </li>
        <li>
          <svg viewBox="0 0 10 10" aria-hidden="true"><circle cx="5" cy="5" r="4.6"/><path d="M0.5 5h9M5 0.5v9M2.2 2.5h5.6M2.2 7.5h5.6" stroke="#e3e3e3" stroke-width="0.6" fill="none"/></svg>
          www.rvoelectrical.com.au
        </li>
      </ul>
    </div>
    <div class="licence">Electrical Licence No. 64139</div>
  </section>
</main>
</body>
</html>
```